Design a Banner for an Online Casino

New online casino is requiring a website banner for the homepage.

We will attach the main photo along with the required wording. Feel free to add other images or wording to enhance the banner. We can purchase the licensing to the other images you use.

Creativity welcome. Please No cartoons or cartoon themes.

Keep in mind the viewer will only be looking at the banner for a few seconds and the intent is to have the user click on the banner to play in the casino. (Typical online casino players are males aged 25-60 who are interested in sports and technology).

The website is currently under construction and can be seen at this link in order to get a feel for the theme of the site. http://kvl.lantern-moss.com/home.aqp (the current banners are only fill ins, and will be replaced).

Main banner size will be 1030x400

Would also like the same banner in a square 400x400, rectangle 330x200 and a vertical 120x240

Will need files in the editable format, along with JPG and PNG

Feel free to submit multiple designs!

Thank you!!

```html
<!DOCTYPE html>
<html lang="en">
<head>
<meta charset="utf-8">
<title>LuckHarbor.com Online Casino</title>
<link href="https://fonts.googleapis.com/css2?family=Arimo:wght@400;700&family=Roboto+Condensed:wght@400;700&family=Cinzel:wght@700&display=swap" rel="stylesheet">
<style>
  :root {
    --page-bg: #050505;
    --page-bg-soft: #141212;
    --nav-top: #2a2a2a;
    --nav-bottom: #0c0c0c;
    --nav-divider: #3a3a3a;
    --text-white: #ffffff;
    --text-muted: #cfcfcf;
    --field-bg: #101010;
    --accent-red: #d0142f;
    --money-red: #e3102b;
    --money-gold: #f3d27a;
    --dot: #6a6a6a;
    --dot-active: #8ec5ff;
    --scene-dark: #1c1412;
    --scene-warm: #d9a27f;
    --scene-shirt: #efe6e0;
    --scene-dress: #b3182c;
    --scene-table: #2f5f9e;
    --scene-felt: #3f8a5a;
    --scene-pink: #e39aa6;
  }
  * { margin: 0; padding: 0; box-sizing: border-box; }
  html, body { width: 1200px; height: 677px; overflow: hidden; }
  body {
    position: relative;
    background: radial-gradient(ellipse at 50% 60%, var(--page-bg-soft) 0%, var(--page-bg) 70%);
    font-family: "Arimo", Arial, sans-serif;
    color: var(--text-white);
  }

  .account-bar { position: absolute; top: 11px; left: 652px; display: flex; align-items: center; font-size: 11px; font-weight: 700; }
  .account-bar label { margin-right: 4px; }
  .account-bar .field { width: 110px; height: 18px; background: var(--field-bg); border: 1px solid #1c1c1c; margin-right: 18px; }
  .account-bar .field.username { width: 108px; }
  .account-bar .action { margin-right: 14px; }
  .account-bar .action.login { margin-left: 14px; }
  .forgot-link { position: absolute; top: 38px; left: 909px; font-size: 11px; font-weight: 700; color: var(--text-muted); }

  .brand { position: absolute; left: 158px; top: 62px; display: flex; align-items: center; gap: 12px; }
  .brand-mark { width: 52px; height: 52px; background: var(--accent-red); }
  .brand-text { display: flex; flex-direction: column; font-weight: 700; color: var(--text-white); }
  .brand-name { font-size: 34px; line-height: 36px; letter-spacing: 0.5px; }
  .brand-tag { font-size: 13px; letter-spacing: 3px; margin-top: 4px; margin-left: 30px; }

  .main-nav {
    position: absolute; left: 132px; top: 164px; width: 936px; height: 46px;
    background: linear-gradient(var(--nav-top), var(--nav-bottom));
    display: flex; align-items: center; padding-left: 24px;
    font-size: 13px; font-weight: 700;
  }
  .main-nav a { color: var(--text-white); text-decoration: none; padding: 0 22px; line-height: 46px; border-right: 1px solid var(--nav-divider); }
  .main-nav a:last-child { border-right: none; }
  .main-nav .lang { display: flex; align-items: center; gap: 6px; }
  .main-nav .flag { width: 14px; height: 9px; background: linear-gradient(#c8102e 0 50%, #1b3a8a 50%); }

  .hero { position: absolute; left: 140px; top: 220px; width: 923px; height: 359px; overflow: hidden; background: var(--scene-dark); }
  .hero-photo {
    position: absolute; inset: 0;
    background:
      radial-gradient(ellipse 150px 120px at 14% 72%, var(--scene-shirt) 0%, rgba(239,230,224,0.55) 45%, transparent 100%),
      radial-gradient(ellipse 110px 80px at 28% 92%, var(--scene-table) 0%, rgba(47,95,158,0.5) 50%, transparent 100%),
      radial-gradient(ellipse 170px 60px at 56% 94%, var(--scene-felt) 0%, rgba(63,138,90,0.45) 50%, transparent 100%),
      radial-gradient(ellipse 100px 140px at 47% 62%, var(--scene-dress) 0%, rgba(179,24,44,0.5) 50%, transparent 100%),
      radial-gradient(ellipse 240px 120px at 40% 30%, var(--scene-warm) 0%, rgba(217,162,127,0.55) 45%, transparent 100%),
      radial-gradient(ellipse 130px 150px at 90% 50%, var(--scene-pink) 0%, rgba(227,154,166,0.45) 45%, transparent 100%),
      radial-gradient(ellipse 120px 90px at 68% 30%, #b8836a 0%, transparent 100%),
      linear-gradient(90deg, #4a3a34 0%, #2e2220 35%, #221a18 65%, #3a2a28 100%);
  }
  .hero-copy { position: absolute; left: 647px; top: 163px; font-family: "Roboto Condensed", Arial, sans-serif; color: var(--text-white); text-shadow: 0 1px 3px rgba(0,0,0,0.6); }
  .hero-copy .line { font-size: 19px; line-height: 22px; letter-spacing: 0.3px; }
  .hero-copy .big { font-size: 32px; line-height: 32px; color: var(--accent-red); font-weight: 700; }
  .hero-copy .red-word { color: var(--accent-red); font-size: 25px; font-weight: 700; }
  .money-badge {
    position: absolute; left: 611px; top: 281px; width: 254px; height: 56px;
    background: var(--money-red); display: flex; align-items: center; justify-content: center;
    font-family: "Cinzel", Georgia, serif; font-size: 44px; font-weight: 700; color: var(--money-gold); letter-spacing: 1px;
  }

  .slider-dots { position: absolute; top: 587px; left: 574px; display: flex; gap: 12px; }
  .slider-dots span { width: 9px; height: 9px; border-radius: 50%; background: var(--dot); }
  .slider-dots span.active { background: var(--dot-active); }

  .game-tiles { position: absolute; top: 648px; left: 141px; display: flex; gap: 17px; }
  .game-tile { position: relative; width: 295px; height: 40px; background: linear-gradient(90deg, #2b2b2b, #4a3a34); overflow: hidden; }
  .game-tile span { position: absolute; top: 2px; font-size: 26px; color: var(--text-white); }
  .game-tile.poker span { left: 6px; }
  .game-tile.casino span, .game-tile.sports span { right: 8px; }
</style>
</head>
<body>
  <div class="account-bar">
    <label>Username:</label><div class="field username"></div>
    <label>Password:</label><div class="field"></div>
    <span class="action login">Login</span><span class="action">Register</span>
  </div>
  <div class="forgot-link">Forgot your username or password?</div>

  <div class="brand">
    <div class="brand-mark"></div>
    <div class="brand-text">
      <span class="brand-name">LuckHarbor.com</span>
      <span class="brand-tag">ONLINE CASINO</span>
    </div>
  </div>

  <nav class="main-nav">
    <a>HOME</a><a>REGISTER</a><a>PROMOTIONS</a><a>GAMES</a><a>LOYALTY CLUB</a><a>MOBILE</a><a>SUPPORT</a>
    <a class="lang"><span class="flag"></span>English</a>
  </nav>

  <section class="hero">
    <div class="hero-photo" role="img" aria-label="Group of friends celebrating around a casino table with chips and cocktails"></div>
    <div class="hero-copy">
      <div class="line">IT PAY TO HAVE</div>
      <div class="big">FRIENDS</div>
      <div class="line" style="margin-top:6px">REFER A <span class="red-word">FRIEND</span> TODAY</div>
      <div class="line">AND START EARNING</div>
    </div>
    <div class="money-badge">MONEY</div>
  </section>

  <div class="slider-dots"><span class="active"></span><span></span><span></span></div>

  <div class="game-tiles">
    <div class="game-tile poker" role="img" aria-label="Poker player photo"><span>Poker</span></div>
    <div class="game-tile casino" role="img" aria-label="Casino player photo"><span>Casino</span></div>
    <div class="game-tile sports" role="img" aria-label="Football match photo"><span>Sports</span></div>
  </div>
</body>
</html>
```